Lantern Hearthworks Business Cards

Looking to create simple business cards that highlight our unique three sided triangle fire pit design with the colors and font of our logo, listed below.

Requirements
Must have
• Looking for something simple that includes a picture of our fire pit with name, website (lanternhearthworks.com), phone number and email. Want to keep the color mostly orange and black.
• Font is gotham(medium) and orange color code is #ee6e22

```html
<!DOCTYPE html>
<html lang="en">
<head>
<meta charset="utf-8">
<title>Lantern Hearthworks Business Cards</title>
<link href="https://fonts.googleapis.com/css2?family=Montserrat:wght@400;500;600&display=swap" rel="stylesheet">
<style>
  :root {
    --backdrop: #3b322d;
    --card: #0d0d0e;
    --card-edge: #1a1a1b;
    --orange: #ee6e22;
    --white: #f4f4f4;
    --muted: #bdbdbd;
    --pit-dark: #1c1b1b;
    --fire-mid: #c8480f;
    --fire-hot: #f59a3c;
  }
  * { margin: 0; padding: 0; box-sizing: border-box; }
  html, body { width: 1200px; height: 847px; overflow: hidden; }
  body {
    background: var(--backdrop);
    font-family: "Montserrat", Arial, sans-serif;
    position: relative;
  }
  .card {
    position: absolute;
    top: 268px;
    width: 540px;
    height: 310px;
    background: var(--card);
    border: 1px solid var(--card-edge);
    box-shadow: 0 14px 30px rgba(0,0,0,.45);
    overflow: hidden;
  }
  .card--front { left: 40px; }
  .card--back { left: 620px; }

  /* Front */
  .pit-photo {
    position: absolute;
    left: 160px;
    top: 40px;
    width: 230px;
    height: 160px;
    border-radius: 6px;
    background:
      radial-gradient(ellipse 55% 45% at 58% 42%, var(--fire-hot) 0%, var(--fire-mid) 40%, rgba(200,72,15,0) 75%),
      linear-gradient(160deg, var(--pit-dark) 0%, #121212 100%);
  }
  .front-wordmark {
    position: absolute;
    right: 36px;
    bottom: 34px;
    text-align: right;
    color: var(--orange);
    font-weight: 500;
    font-size: 22px;
    letter-spacing: 4px;
    line-height: 1.2;
    text-transform: uppercase;
  }

  /* Back */
  .back-header {
    position: absolute;
    top: 38px;
    left: 110px;
    display: flex;
    align-items: center;
    gap: 18px;
  }
  .brand-dot {
    width: 56px;
    height: 56px;
    border-radius: 50%;
    background: var(--orange);
  }
  .back-header .divider {
    width: 1px;
    height: 62px;
    background: var(--muted);
  }
  .back-wordmark {
    color: var(--orange);
    font-weight: 500;
    font-size: 20px;
    letter-spacing: 4px;
    line-height: 1.2;
    text-transform: uppercase;
  }
  .holder {
    position: absolute;
    left: 40px;
    top: 132px;
  }
  .holder-name {
    color: var(--orange);
    font-weight: 600;
    font-size: 22px;
    letter-spacing: 1px;
    text-transform: uppercase;
  }
  .holder-title {
    color: var(--white);
    font-size: 14px;
    margin-top: 2px;
  }
  .contacts {
    position: absolute;
    left: 40px;
    top: 200px;
    list-style: none;
  }
  .contacts li {
    display: flex;
    align-items: center;
    gap: 12px;
    color: var(--white);
    font-size: 14px;
    height: 26px;
  }
  .contacts svg { width: 14px; height: 14px; flex: none; }
  .contacts .accent { color: var(--orange); }
</style>
</head>
<body>

  <section class="card card--front">
    <div class="pit-photo" role="img" aria-label="Photograph of the three-sided triangle fire pit with logs burning"></div>
    <div class="front-wordmark">Lantern<br>Hearthworks</div>
  </section>

  <section class="card card--back">
    <header class="back-header">
      <span class="brand-dot" aria-hidden="true"></span>
      <span class="divider"></span>
      <div class="back-wordmark">Lantern<br>Hearthworks</div>
    </header>

    <div class="holder">
      <div class="holder-name">Mara Ellison</div>
      <div class="holder-title">Founder &amp; CEO</div>
    </div>

    <ul class="contacts">
      <li>
        <svg viewBox="0 0 24 24" aria-hidden="true"><path fill="#ee6e22" d="M6.6 10.8a15 15 0 0 0 6.6 6.6l2.2-2.2a1 1 0 0 1 1-.25 11.4 11.4 0 0 0 3.6.57 1 1 0 0 1 1 1V20a1 1 0 0 1-1 1A17 17 0 0 1 3 4a1 1 0 0 1 1-1h3.5a1 1 0 0 1 1 1c0 1.25.2 2.45.57 3.6a1 1 0 0 1-.25 1z"/></svg>
        123 456 7890
      </li>
      <li>
        <svg viewBox="0 0 24 24" aria-hidden="true"><path fill="#ee6e22" d="M2 5h20v14H2z"/><path fill="none" stroke="#0d0d0e" stroke-width="2" d="M2 5l10 8 10-8"/></svg>
        hello@lanternhearthworks.com
      </li>
      <li>
        <svg viewBox="0 0 24 24" aria-hidden="true"><circle cx="12" cy="12" r="10" fill="none" stroke="#ee6e22" stroke-width="2"/><path fill="none" stroke="#ee6e22" stroke-width="1.6" d="M2 12h20M12 2c3 3 3 17 0 20M12 2c-3 3-3 17 0 20"/></svg>
        <span>www.<span class="accent">lanternhearthworks</span>.com</span>
      </li>
    </ul>
  </section>

</body>
</html>
```